Website re-design

We are a successful furnished apartment provider in Boston. We currently are working on re-designing our website www.ribtenlofts.com to make it more modern, designer look and user friendly. We hired a designer, but are not happy with the designs proposed and want to improve on them. The winning design will be paid regardless of whether we stay with our current designer or not. We want ideas and functional page links to see how it will work. Platform we have chosen is wordpress. Feel free to propose others easy for us to update and modify. We do not like Joomla on which website is currently running. We do not like flash nor long load times.
Please use photos on our website for design presentations. www.ribtenlofts.com

Target Market(s)

doctors, nurses, business men but mostly business women, some post-medical students

Industry/Entity Type

Apartment

Requirements
Must have
• Quick action button for reservation form and a notification and email forwarding system to us of reservation information by potential clients. Blog required with feedback by guests allowed, we can censor which are published. Slide shows of apartments.
Should not have
• No movies.

```html
<!DOCTYPE html>
<html lang="en">
<head>
<meta charset="utf-8">
<title>Ribten Lofts – Furnished Apartment</title>
<link rel="stylesheet" href="https://fonts.googleapis.com/css2?family=Marcellus&family=Arimo:ital,wght@0,400;0,700;1,400&display=swap">
<style>
:root{
  --blue:#2f8bbd;
  --blue-dark:#1f6f9e;
  --gold:#a8924e;
  --gold-light:#d9c68a;
  --ink:#111;
  --text:#444;
  --link:#2a8bc4;
  --page:#ececec;
  --side:#e2e2e2;
  --footer:#1d1d1d;
  --green:#7cbf3c;
  --white:#fff;
}
*{box-sizing:border-box;margin:0;padding:0}
html,body{width:808px;height:1200px;overflow:hidden}
body{position:relative;background:var(--page);font-family:"Arimo",Arial,sans-serif;color:var(--text)}
.abs{position:absolute}
.topline{left:0;top:0;width:808px;height:9px;background:var(--blue)}
.header{left:0;top:9px;width:808px;height:103px;background:var(--white)}
.hero-band{left:0;top:112px;width:808px;height:259px;background:linear-gradient(#3a97c8,#2a82b4)}
.brand{display:flex;align-items:center;gap:12px}
.brand-mark{width:50px;height:50px;border-radius:50%;background:var(--gold);flex:none}
.brand-name{font-family:"Marcellus",serif;color:var(--ink);font-size:24px;line-height:1;letter-spacing:.3px}
.brand-tag{font-family:"Marcellus",serif;color:var(--ink);font-size:11px;letter-spacing:.5px;margin-top:5px}
.nav{right:31px;top:44px;display:flex;font-family:"Marcellus",serif;font-size:10.5px;color:#222}
.nav a{color:#222;text-decoration:none;padding:0 4px;border-left:1px solid #444;line-height:11px}
.nav a:first-child{border:0;color:var(--gold);font-size:12.5px}
.nav a:last-child{padding-right:0}
.dropdown{left:517px;top:70px;width:83px;height:72px;background:#f3f3f3;border-radius:4px;box-shadow:0 2px 5px rgba(0,0,0,.35);z-index:3;font-family:"Marcellus",serif;font-size:9px;color:#2a6f96;text-align:center}
.dropdown div{height:22px;line-height:22px;border-bottom:1px solid #d5d5d5;margin:0 3px}
.dropdown div:last-child{border:0}
.slider{left:31px;top:92px;width:747px;height:229px;background:var(--white);box-shadow:0 3px 8px rgba(0,0,0,.35)}
.slide-photo{left:7px;top:7px;width:733px;height:218px;background:linear-gradient(160deg,#c9b596 0%,#8a6c4a 40%,#2e2a4a 65%,#a67a45 100%)}
.reserve{left:14px;top:183px;width:182px;height:35px;border-radius:18px;background:linear-gradient(#d7c68e,#9d8644);color:var(--white);font-family:"Marcellus",serif;font-size:19px;letter-spacing:1px;text-align:center;line-height:35px;border:1px solid #e6d9a8}
.dots{left:366px;top:349px;display:flex;gap:8px}
.dots span{width:13px;height:13px;border-radius:50%;border:2px solid #8fc3df;background:#2a7fae}
.sidebar{left:539px;top:371px;width:238px;height:578px;background:var(--side)}
.welcome{left:33px;top:403px;font-family:"Marcellus",serif;font-size:22px;color:var(--ink)}
.welcome small{font-size:17px}
.intro{left:33px;top:438px;width:494px;font-size:9.4px;line-height:11.3px;color:#555}
.intro p{margin-bottom:11px}
.card{width:160px}
.card-thumb{width:143px;height:106px;background:var(--white);padding:5px;box-shadow:0 1px 3px rgba(0,0,0,.25)}
.card-thumb div{width:100%;height:100%;background:linear-gradient(#cfd6da,#8d8f86 60%,#5c6b3e)}
.card h3{font-size:10px;color:var(--ink);margin:15px 0 6px 2px;font-weight:400}
.card p{font-size:8.3px;line-height:14.3px;color:#555;margin-left:2px;width:138px}
.more{color:var(--link);font-weight:700;font-size:8.5px;text-align:right;display:block}
.card .more{width:131px;margin-top:1px}
.side-h{font-family:"Arimo",sans-serif;color:var(--blue-dark);font-size:15px;font-weight:400}
.search{left:554px;top:427px;width:203px;height:20px;border:1px solid #ccc;border-radius:10px;background:var(--white);font-size:8.5px;font-style:italic;color:#888;line-height:18px;padding-left:10px}
.search-btn{right:-1px;top:-1px;width:24px;height:20px;border-radius:0 10px 10px 0;background:var(--blue)}
.rule{height:1px;background:#cfcfcf}
.news{left:554px;width:206px;height:92px}
.badge{left:3px;top:0;width:33px;height:36px;border-radius:4px;background:var(--white);box-shadow:0 1px 3px rgba(0,0,0,.3);overflow:hidden;text-align:center}
.badge b{display:block;height:12px;background:var(--green);color:var(--white);font-size:8px;line-height:12px}
.badge span{display:block;font-family:"Arimo",sans-serif;color:var(--blue);font-size:14px;line-height:22px}
.news h4{position:absolute;left:47px;top:3px;font-size:9.8px;color:var(--blue-dark);font-weight:400}
.news p{position:absolute;left:47px;top:17px;width:132px;font-size:8.3px;line-height:14.3px;color:#555}
.news .more{position:absolute;right:26px;top:66px}
.news .rule{position:absolute;left:0;bottom:0;width:206px}
.footer{left:0;top:949px;width:808px;height:216px;background:var(--footer)}
.foot-brand .brand-name,.foot-brand .brand-tag{color:var(--gold-light)}
.foot-text{font-size:9.8px;line-height:11.5px;color:var(--white)}
.foot-h{font-family:"Marcellus",serif;font-size:14px;color:var(--gold-light)}
.social{left:32px;top:1106px;display:flex;gap:3px}
.social span{width:18px;height:18px;border-radius:3px;background:#3d84b8}
.testi{left:317px;width:220px}
.testi em{display:block;font-size:8px;color:#999;margin-top:5px}
.contact-row{left:602px;display:flex;gap:9px}
.contact-row svg{flex:none;margin-top:1px}
.bottombar{left:0;top:1165px;width:808px;height:35px;background:linear-gradient(#3a97c8,#2a82b4);font-family:"Marcellus",serif;font-size:10.5px;color:var(--white)}
.bottom-nav{right:31px;top:11px;display:flex}
.bottom-nav a{color:var(--white);text-decoration:none;padding:0 9px;border-left:1px solid #bfe0f1}
.bottom-nav a:first-child{border:0}
.bottom-nav a:last-child{padding-right:0}
</style>
</head>
<body>
<div class="abs topline"></div>
<header class="abs header">
  <div class="abs brand" style="left:31px;top:16px">
    <div class="brand-mark"></div>
    <div><div class="brand-name">RIBTEN LOFTS</div><div class="brand-tag">FURNISHED APARTMENT</div></div>
  </div>
  <nav class="abs nav">
    <a href="#">Home</a><a href="#">About Us</a><a href="#">Apartments</a><a href="#">Boston</a><a href="#">Reservations</a><a href="#">Blog</a><a href="#">Reviews</a><a href="#">Contact Us</a>
  </nav>
</header>
<div class="abs dropdown"><div>One Column</div><div>Two Columns</div><div>Three Columns</div></div>
<div class="abs hero-band"></div>
<section class="abs slider">
  <div class="abs slide-photo" role="img" aria-label="Photo of a furnished apartment bedroom with bed, armchairs and desk"></div>
  <div class="abs reserve">RESERVE NOW</div>
</section>
<div class="abs dots"><span></span><span></span><span></span><span></span></div>

<aside class="abs sidebar"></aside>

<h1 class="abs welcome"><small>WELLCOME TO </small>RIBTEN LOFTS</h1>
<div class="abs intro">
  <p>Lorem Ipsum is simply dummy text of the printing and typesetting industry. Lorem Ipsum has been the industry's standard dummy text ever since the 1500s, when an unknown printer took a galley of type and scrambled it to make a type specimen book. It has survived not only five centuries, but also the leap into electronic typesetting, remaining essentially unchanged. It was popularised in the 1960s with the release of Typeline sheets containing Lorem Ipsum passages, and more recently with desktop publishing software like Folio LayoutPro including versions of Lorem Ipsum.</p>
  <p>It is a long established fact that a reader will be distracted by the readable content of a page when looking at its layout. The point of using Lorem Ipsum is that it has a more-or-less normal distribution of letters, as opposed to using 'Content here, content here', making it look like readable English.</p>
  <p>Lorem Ipsum is simply dummy text of the printing and typesetting industry. Lorem Ipsum has been the industry's standard dummy text ever since the 1500s, when an unknown printer took a galley of type and scrambled it to make a type specimen book. It has survived not only five centuries, but also the leap into electronic typesetting, remaining essentially unchanged. It was popularised in the 1960s with the release of Typeline sheets containing Lorem Ipsum passages, and more recently with desktop publishing software like Folio LayoutPro including versions of Lorem Ipsum.</p>
  <p>Many desktop publishing packages and web page editors now use Lorem Ipsum as their default model text, and a search for 'lorem ipsum' will uncover many web sites......</p>
</div>

<article class="abs card" style="left:40px;top:703px">
  <div class="card-thumb"><div role="img" aria-label="Photo of a modern white apartment building"></div></div>
  <h3>Lorem Ipsum dolor sit amet</h3>
  <p>Lorem Ipsum is simply dummy text of the printing and typesetting industry.</p>
  <a class="more">Read More</a>
</article>
<article class="abs card" style="left:206px;top:703px">
  <div class="card-thumb"><div role="img" aria-label="Photo of a modern red and white residential building"></div></div>
  <h3>Lorem Ipsum dolor sit amet</h3>
  <p>Lorem Ipsum is simply dummy text of the printing and typesetting industry.</p>
  <a class="more">Read More</a>
</article>
<article class="abs card" style="left:372px;top:703px">
  <div class="card-thumb"><div role="img" aria-label="Photo of a modern building with palm trees"></div></div>
  <h3>Lorem Ipsum dolor sit amet</h3>
  <p>Lorem Ipsum is simply dummy text of the printing and typesetting industry.</p>
  <a class="more">Read More</a>
</article>

<h2 class="abs side-h" style="left:554px;top:403px">Search</h2>
<div class="abs search">Search Here
  <div class="abs search-btn"><svg width="24" height="20" viewBox="0 0 24 20"><circle cx="11" cy="9" r="3.5" fill="none" stroke="#fff" stroke-width="1.5"/><line x1="13.5" y1="11.5" x2="16" y2="14" stroke="#fff" stroke-width="1.6"/></svg></div>
</div>
<div class="abs rule" style="left:554px;top:471px;width:206px"></div>
<h2 class="abs side-h" style="left:554px;top:492px">Latest News/Events:</h2>
<div class="abs" style="left:555px;top:512px;font-size:8px;font-style:italic;color:#888">Lorem ipsum dolor sit amet, consectetur.</div>

<div class="abs news" style="top:536px">
  <div class="abs badge"><b>NOV</b><span>05</span></div>
  <h4>Lorem Ipsum dolor sit amet</h4>
  <p>Lorem Ipsum is simply dummy text of the printing and typesetting industry.</p>
  <a class="more">Read More</a><div class="rule"></div>
</div>
<div class="abs news" style="top:631px">
  <div class="abs badge"><b>NOV</b><span>08</span></div>
  <h4>Lorem Ipsum dolor sit amet</h4>
  <p>Lorem Ipsum is simply dummy text of the printing and typesetting industry.</p>
  <a class="more">Read More</a><div class="rule"></div>
</div>
<div class="abs news" style="top:727px">
  <div class="abs badge"><b>NOV</b><span>15</span></div>
  <h4>Lorem Ipsum dolor sit amet</h4>
  <p>Lorem Ipsum is simply dummy text of the printing and typesetting industry.</p>
  <a class="more">Read More</a><div class="rule"></div>
</div>
<div class="abs news" style="top:822px">
  <div class="abs badge"><b>NOV</b><span>15</span></div>
  <h4>Lorem Ipsum dolor sit amet</h4>
  <p>Lorem Ipsum is simply dummy text of the printing and typesetting industry.</p>
  <a class="more">Read More</a><div class="rule"></div>
</div>

<footer class="abs footer"></footer>
<div class="abs brand foot-brand" style="left:31px;top:959px">
  <div class="brand-mark" style="width:48px;height:48px"></div>
  <div><div class="brand-name">RIBTEN LOFTS</div><div class="brand-tag">FURNISHED APARTMENT</div></div>
</div>
<div class="abs foot-text" style="left:33px;top:1015px;width:215px">Lorem Ipsum is simply dummy text of the printing and typesetting industry. Lorem Ipsum has been the industry's standard dummy.<br>Lorem Ipsum is simply dummy text of the printing and typesetting industry.</div>
<div class="abs foot-h" style="left:33px;top:1084px">Follow Us:</div>
<div class="abs social"><span></span><span></span><span></span><span></span><span></span><span></span><span></span></div>

<div class="abs foot-h" style="left:317px;top:966px">Client Testimonials:</div>
<div class="abs testi foot-text" style="top:990px">Lorem Ipsum is simply dummy text of the printing and typesetting industry. Lorem Ipsum has been the industry's standard dummy.....<em>about 3 days ago</em></div>
<div class="abs testi foot-text" style="top:1050px">Lorem Ipsum is simply dummy text of the printing and typesetting industry.....<em>about 3 days ago</em></div>
<div class="abs testi foot-text" style="top:1097px">Lorem Ipsum is simply dummy text of the printing and typesetting industry. Lorem Ipsum has been the industry's standard dummy.....<em>about 3 days ago</em></div>

<div class="abs foot-h" style="left:602px;top:966px">Contact Us:</div>
<div class="abs contact-row foot-text" style="top:989px">
  <svg width="12" height="11" viewBox="0 0 12 11"><path d="M1 6 6 1l5 5H9.5v5h-7V6z" fill="#bbb"/></svg>
  <div>Address Comes here....<br>Address Comes here....</div>
</div>
<div class="abs contact-row foot-text" style="top:1022px">
  <svg width="12" height="11" viewBox="0 0 12 11"><circle cx="6" cy="5.5" r="4.5" fill="none" stroke="#bbb" stroke-width="1.5"/><circle cx="6" cy="5.5" r="1.5" fill="#bbb"/></svg>
  <div>Address Comes here....</div>
</div>
<div class="abs contact-row foot-text" style="top:1042px">
  <svg width="12" height="11" viewBox="0 0 12 11"><path d="M2 1h3l1 2.5-1.5 1a6 6 0 0 0 3 3l1-1.5L11 7v3c-5 0-9-4-9-9z" fill="#bbb"/></svg>
  <div>Phone: +000 000 0000<br>Fax: +000 000 0000<br>Mobile: +000 000 0000</div>
</div>
<div class="abs contact-row foot-text" style="top:1090px">
  <svg width="12" height="11" viewBox="0 0 12 11"><rect x="1" y="2" width="10" height="7" fill="none" stroke="#bbb"/><path d="M1 2l5 4 5-4" fill="none" stroke="#bbb"/></svg>
  <div>dummy@loftmailbox.com<br>info@loftmailbox.com</div>
</div>

<div class="abs bottombar">
  <div class="abs" style="left:35px;top:11px">©2012 Ribten Lofts Furnished Apartment &nbsp;|&nbsp; All Rights Reserved</div>
  <nav class="abs bottom-nav"><a href="#">Home</a><a href="#">Projects</a><a href="#">About Us</a><a href="#">Contact Us</a></nav>
</div>
</body>
</html>
```